Real Estate investment company needs billboard designs

This is our website: https://velmarkpropertygroup.com/
We are looking for some billboard concepts that uses our CEO in the design. I have attached some images and 1 billboard design that someone in our industry uses, but we don't want it exactly like his.

Industry/Entity Type

real estate

Colors

Designer to choose colors to be used in the design.

Requirements
Must have
• Company colors from websiute

```html
<!DOCTYPE html>
<html lang="en">
<head>
<meta charset="utf-8">
<title>Velmark Property Group – Billboard</title>
<link href="https://fonts.googleapis.com/css2?family=Anton&family=Tinos:wght@400;700&display=swap" rel="stylesheet">
<style>
  :root {
    --backdrop: #dfe6ee;
    --navy: #1e2147;
    --navy-deep: #151735;
    --accent-red: #d6313a;
    --tan: #d9bb8c;
    --white: #ffffff;
    --muted: #c9cbd8;
    --rule: rgba(255,255,255,.28);
  }
  * { margin: 0; padding: 0; box-sizing: border-box; }
  html, body {
    width: 1200px; height: 900px; overflow: hidden;
    background: var(--backdrop);
  }
  .billboard {
    position: absolute; left: 40px; top: 177px;
    width: 1120px; height: 546px;
    overflow: hidden;
    background: var(--navy);
    box-shadow: 0 6px 18px rgba(0,0,0,.18);
  }
  .billboard-art { position: absolute; inset: 0; display: block; }

  .brand {
    position: absolute; left: 52px; top: 40px;
    display: flex; align-items: center; gap: 12px;
  }
  .brand-mark { width: 18px; height: 18px; background: var(--accent-red); }
  .brand-name {
    font-family: "Tinos", serif; font-weight: 700;
    font-size: 26px; line-height: 1; color: var(--white); letter-spacing: .4px;
  }

  .headline {
    position: absolute; left: 52px; top: 96px;
    font-family: "Anton", sans-serif; color: var(--white);
  }
  .headline-main { font-size: 72px; line-height: 1.1; letter-spacing: .2px; }
  .headline-sub {
    font-size: 19px; letter-spacing: .6px; color: var(--tan); margin-top: 6px;
  }
  .headline-sub .divider {
    display: inline-block; width: 2px; height: 16px; background: var(--accent-red);
    margin: 0 12px; vertical-align: -1px;
  }

  .offer-copy {
    position: absolute; left: 52px; top: 268px;
    border-left: 3px solid var(--accent-red); padding-left: 14px;
    font-family: "Tinos", serif; font-weight: 700; letter-spacing: .4px;
  }
  .offer-copy .accent { color: var(--tan); font-size: 24px; line-height: 1.3; }
  .offer-copy .plain { color: var(--white); font-size: 19px; line-height: 1.35; }

  .call-block {
    position: absolute; left: 52px; top: 378px;
    width: 470px; height: 124px;
    display: flex; align-items: center; gap: 20px;
    padding: 0 24px;
    background: var(--navy-deep);
    border: 1px solid var(--rule);
    font-family: "Tinos", serif; font-weight: 700; letter-spacing: .4px;
  }
  .call-icon {
    flex: 0 0 60px; width: 60px; height: 60px; border-radius: 50%;
    background: var(--accent-red);
    display: flex; align-items: center; justify-content: center;
  }
  .call-label { color: var(--tan); font-size: 19px; line-height: 1.2; }
  .call-phone { color: var(--white); font-size: 40px; line-height: 1.15; }
  .call-note { color: var(--muted); font-size: 16px; line-height: 1.3; }
</style>
</head>
<body>
  <main class="billboard">
    <svg class="billboard-art" viewBox="0 0 1120 546" xmlns="http://www.w3.org/2000/svg">
      <defs>
        <linearGradient id="houseFill" x1="0" y1="0" x2="0" y2="1">
          <stop offset="0" stop-color="#dbe3ea"/>
          <stop offset=".6" stop-color="#eef0f1"/>
          <stop offset=".82" stop-color="#8aa86a"/>
          <stop offset="1" stop-color="#6f9a3e"/>
        </linearGradient>
        <linearGradient id="ceoFill" x1="0" y1="0" x2="0" y2="1">
          <stop offset="0" stop-color="#b8a390"/>
          <stop offset=".45" stop-color="#8f7a69"/>
          <stop offset="1" stop-color="#2c2f4a"/>
        </linearGradient>
      </defs>

      <polygon class="photo-house" role="img"
        aria-label="Photo of a white house with a dark roof, porch stairs and a green lawn"
        points="640,0 1120,0 1120,546 560,546" fill="url(#houseFill)"/>
      <polygon class="photo-edge" points="632,0 644,0 564,546 552,546" fill="#d6313a"/>

      <path class="photo-ceo" role="img"
        aria-label="Portrait of the company CEO in business attire, smiling toward the viewer"
        d="M780 546 L780 250 Q780 70 915 70 Q1050 70 1050 250 L1050 546 Z"
        fill="url(#ceoFill)"/>
    </svg>

    <div class="brand">
      <span class="brand-mark"></span>
      <span class="brand-name">Velmark Property Group</span>
    </div>

    <div class="headline">
      <div class="headline-main">SELL YOUR HOME</div>
      <div class="headline-sub">GET YOUR CASH OFFER<span class="divider"></span>SELL YOUR HOUSE FAST</div>
    </div>

    <div class="offer-copy">
      <div class="accent">Get Your FREE Offer.</div>
      <div class="plain">Same Day, No Obligations, Just Options.</div>
    </div>

    <div class="call-block">
      <div class="call-icon">
        <svg width="30" height="30" viewBox="0 0 24 24" aria-hidden="true">
          <path fill="#ffffff" d="M6.6 10.8a15.1 15.1 0 0 0 6.6 6.6l2.2-2.2a1 1 0 0 1 1-.25 11.4 11.4 0 0 0 3.6.57 1 1 0 0 1 1 1V20a1 1 0 0 1-1 1A17 17 0 0 1 3 4a1 1 0 0 1 1-1h3.5a1 1 0 0 1 1 1c0 1.25.2 2.45.57 3.6a1 1 0 0 1-.25 1z"/>
        </svg>
      </div>
      <div class="call-text">
        <div class="call-label">Call Now</div>
        <div class="call-phone">555-210-4837</div>
        <div class="call-note">Get a Cash Offer, Same Day</div>
      </div>
    </div>
  </main>
</body>
</html>
```